Conference for Teenagers Needs Event Graphics

I am in need of event graphics for our upcoming event. This event, titled "Maple Ridge Youth Conference", is a weekend event for teenagers 11-19 years old. They hear from speakers, listen to a band, and do other fun activities. Our theme is "Together." Graphic design should have a young adult/older teen feel. Clean, not very bright colors.

Event Info:
November 6-8, 2020
Velmora Exhibit Hall, Ashbrook Falls, PA
Speakers: TBD (will give name and picture before final approval)
Worship: (band name TBD before final approval)
MapleRidgeYC-event.com
#872MR
Our Organization Logo (attached): PA Crestway

Once designed, I need the following graphics file sizes:
-11x17 Vertical Poster design: include all event info AND a "blank" spot/box for groups to add their own details/information. Also include the KRV logo and our organization logo PA Crestway in someway.
-4x3 horizontal postcard: include all event info on 1 side including PACrestway logo and KRV; blank backside
-Main Graphic Slide: formatted to fit a widescreen 16x9 screen. Include event name, hashtag, KRV and PA Crestway logo
-social media graphics for event: can incorporate some or all of the event details
-4.25x 2.75 vertical badge: include event title on front with PA Crestway logo

Target Market(s)

Young adults or older teenagers

Requirements
Must have
• -event info
-PA Crestway Logo & KRV logo

```html
<!DOCTYPE html>
<html lang="en">
<head>
<meta charset="utf-8">
<title>Maple Ridge Youth Conference – Poster</title>
<link rel="stylesheet" href="https://fonts.googleapis.com/css2?family=Krona+One&family=Lexend:wght@300;400;600&display=swap">
<style>
  :root {
    --backdrop: #93c1ec;
    --poster-blue: #2d549b;
    --haze-blue: #3f63a8;
    --ink: #ffffff;
    --portrait-light: #f2f2f2;
    --portrait-mid: #c9c4c0;
  }
  * { margin: 0; padding: 0; box-sizing: border-box; }
  html, body {
    width: 1200px; height: 1200px; overflow: hidden;
    background: var(--backdrop);
  }
  .poster {
    position: absolute; left: 199px; top: 82px;
    width: 801px; height: 1035px;
    background: var(--poster-blue);
    color: var(--ink);
    font-family: "Lexend", sans-serif;
    font-weight: 300;
    overflow: hidden;
  }
  .crowd-photo {
    position: absolute; inset: 0;
    background:
      radial-gradient(ellipse 200px 260px at 40% 18%, rgba(156,143,180,.55), transparent 70%),
      radial-gradient(ellipse 260px 200px at 62% 52%, rgba(156,143,180,.5), transparent 70%),
      radial-gradient(ellipse 220px 300px at 25% 75%, rgba(156,143,180,.45), transparent 70%),
      radial-gradient(ellipse 240px 220px at 85% 30%, rgba(156,143,180,.35), transparent 70%),
      radial-gradient(ellipse 300px 240px at 75% 85%, rgba(156,143,180,.4), transparent 70%),
      linear-gradient(180deg, var(--haze-blue), var(--poster-blue));
  }
  .content { position: absolute; inset: 0; }
  .partner-marks {
    position: absolute; left: 50px; top: 46px;
    display: flex; gap: 28px; align-items: center;
    font-size: 24px; font-weight: 600;
  }
  .event-title {
    position: absolute; left: 48px; top: 142px;
    font-family: "Krona One", sans-serif;
    font-weight: 400;
    font-size: 58px; line-height: 76px;
    text-transform: uppercase;
    color: transparent;
    -webkit-text-stroke: 2.5px var(--ink);
    letter-spacing: 1px;
    white-space: nowrap;
  }
  .event-details {
    position: absolute; left: 57px; top: 400px;
    font-size: 30px; line-height: 48px; font-weight: 300;
  }
  .section-divider {
    position: absolute; left: 47px; width: 706px;
    display: flex; align-items: center; gap: 18px;
    font-size: 28px; font-weight: 300;
  }
  .section-divider::before, .section-divider::after {
    content: ""; flex: 1; height: 3px; background: var(--ink);
  }
  .speakers-heading { top: 532px; }
  .worship-heading { top: 802px; }
  .speaker {
    position: absolute; top: 592px; width: 180px;
    text-align: center; font-size: 22px; font-weight: 300;
  }
  .speaker-portrait {
    width: 122px; height: 122px; border-radius: 50%;
    margin: 0 auto 26px;
    background: radial-gradient(circle at 50% 40%, var(--portrait-mid), var(--portrait-light) 70%);
  }
  .band-name {
    position: absolute; left: 0; right: 0; top: 862px;
    text-align: center;
    font-family: "Krona One", sans-serif;
    font-size: 26px; letter-spacing: 1px;
    text-transform: uppercase;
  }
  .footer {
    position: absolute; left: 47px; right: 48px; top: 968px;
    display: flex; justify-content: space-between;
    font-size: 20px;
  }
  .website { font-style: italic; }
  .hashtag { font-weight: 600; font-style: italic; letter-spacing: 1px; }
</style>
</head>
<body>
  <main class="poster">
    <div class="crowd-photo" role="img" aria-label="Blurred photo of a worship crowd with raised hands, blue toned"></div>
    <div class="content">
      <div class="partner-marks">
        <span class="partner-name">PA Crestway</span>
        <span class="partner-name">KRV</span>
      </div>
      <h1 class="event-title">Maple Ridge<br>Youth<br>Conference</h1>
      <p class="event-details">November 6-8, 2020<br>Velmora Exhibit Hall, Ashbrook Falls, PA</p>

      <div class="section-divider speakers-heading">Speakers</div>
      <div class="speaker" style="left:42px"><div class="speaker-portrait" role="img" aria-label="Portrait of speaker John Doe"></div>John Doe</div>
      <div class="speaker" style="left:220px"><div class="speaker-portrait" role="img" aria-label="Portrait of speaker Jane Roe"></div>Jane Roe</div>
      <div class="speaker" style="left:397px"><div class="speaker-portrait" role="img" aria-label="Portrait of speaker Fred Nerks"></div>Fred Nerks</div>
      <div class="speaker" style="left:575px"><div class="speaker-portrait" role="img" aria-label="Portrait of speaker Hilary Ouse"></div>Hilary Ouse</div>

      <div class="section-divider worship-heading">Worship</div>
      <p class="band-name">Band Name</p>

      <div class="footer">
        <span class="website">MapleRidgeYC-event.com</span>
        <span class="hashtag">#872MR</span>
      </div>
    </div>
  </main>
</body>
</html>
```